Commercial Construction Company

We need a business card design based on our current logo. We are a commercial general contractor based in Southern California that specializes in bank remodels. We would like to see designs that incorporate dark blue. The final design should portray an image of professionalism and quality.

If possible, I would like to add metallic foil to the design. Thank you

```html
<!DOCTYPE html>
<html lang="en">
<head>
<meta charset="utf-8">
<title>Harlow Build Group – Business Card</title>
<link href="https://fonts.googleapis.com/css2?family=Lato:wght@400;700;900&display=swap" rel="stylesheet">
<style>
  :root {
    --backdrop: #c8c8c8;
    --card: #252a33;
    --card-edge: #1b1f26;
    --brand-blue: #1d4e8f;
    --steel: #9a9a9a;
    --text-light: #f2f2f2;
  }
  * { margin: 0; padding: 0; box-sizing: border-box; }
  html, body {
    width: 1200px;
    height: 675px;
    overflow: hidden;
    background: var(--backdrop);
    font-family: "Lato", Arial, sans-serif;
  }
  .stage {
    width: 1200px;
    height: 675px;
    display: flex;
    align-items: center;
    justify-content: center;
    gap: 40px;
  }
  .card {
    width: 540px;
    height: 309px;
    background: var(--card);
    border-radius: 18px;
    box-shadow: 0 4px 0 var(--card-edge), 0 10px 24px rgba(0,0,0,0.25);
    position: relative;
    overflow: hidden;
  }
  .wordmark {
    display: flex;
    align-items: center;
    gap: 12px;
    color: var(--text-light);
    font-weight: 900;
    letter-spacing: 1px;
  }
  .wordmark-dot {
    width: 34px;
    height: 34px;
    border-radius: 50%;
    background: var(--brand-blue);
    flex: none;
  }
  .card-front {
    display: flex;
    align-items: center;
    justify-content: center;
  }
  .card-front .wordmark { font-size: 34px; }
  .card-back {
    display: flex;
    align-items: center;
    padding: 0 30px 0 34px;
  }
  .card-back .wordmark {
    font-size: 24px;
    width: 205px;
    line-height: 1.1;
  }
  .card-back .wordmark-dot { width: 28px; height: 28px; }
  .divider {
    width: 2px;
    height: 190px;
    background: var(--brand-blue);
    margin: 0 24px 0 18px;
    flex: none;
  }
  .contact { color: var(--text-light); font-size: 13.5px; line-height: 1.35; }
  .contact-name {
    color: var(--brand-blue);
    font-weight: 700;
    font-size: 19px;
    text-transform: uppercase;
    letter-spacing: 0.3px;
  }
  .contact-role { font-size: 15px; margin-bottom: 10px; }
  .contact-address { margin-bottom: 10px; }
  .contact-list { list-style: none; }
  .contact-list li { display: flex; align-items: center; gap: 8px; }
  .contact-list svg { width: 13px; height: 13px; fill: var(--brand-blue); flex: none; }
</style>
</head>
<body>
<main class="stage">
  <section class="card card-front" aria-label="Card front">
    <div class="wordmark"><span class="wordmark-dot"></span>HARLOW BUILD GROUP</div>
  </section>

  <section class="card card-back" aria-label="Card back">
    <div class="wordmark"><span class="wordmark-dot"></span>HARLOW BUILD GROUP</div>
    <div class="divider"></div>
    <div class="contact">
      <p class="contact-name">Daniel Reyes</p>
      <p class="contact-role">President</p>
      <p class="contact-address">1420 Harbor Lane, Eastvale<br>CA 91752, United States</p>
      <ul class="contact-list">
        <li><svg viewBox="0 0 16 16" aria-hidden="true"><path d="M3.5 1l2.5 3-1.5 2c1 2 2.5 3.5 4.5 4.5l2-1.5 3 2.5-1.5 2.5C7 14 2 9 1 2.5z"/></svg>000-000-000-000</li>
        <li><svg viewBox="0 0 16 16" aria-hidden="true"><path d="M4 0h8a1 1 0 0 1 1 1v14a1 1 0 0 1-1 1H4a1 1 0 0 1-1-1V1a1 1 0 0 1 1-1zm1 2v10h6V2z"/></svg>000-000-000-000</li>
        <li><svg viewBox="0 0 16 16" aria-hidden="true"><path d="M0 3h16v10H0zm1.5 1.2V5l6.5 4 6.5-4v-.8z"/></svg>info@websitename.com</li>
        <li><svg viewBox="0 0 16 16" aria-hidden="true"><circle cx="8" cy="8" r="7" fill="none" stroke="#1d4e8f" stroke-width="1.5"/><path d="M1 8h14M8 1c-3 4-3 10 0 14M8 1c3 4 3 10 0 14" fill="none" stroke="#1d4e8f" stroke-width="1.2"/></svg>www.websitename.com</li>
      </ul>
    </div>
  </section>
</main>
</body>
</html>
```